Covid 19 Exit Strategy one page brochure

I would like to design, and will need URGENT help, a brochure detailing a Covid 19 Exit Strategy plan. This brochure will need to be understood easily and the graphics inside should make it easy for people to understand without reading the entire text. This project is quite urgent and needs to be completed THIS WEEK - by Saturday may 16th at the latest. I am attaching two examples. I will provide the text.

```html
<!DOCTYPE html>
<html lang="en">
<head>
<meta charset="utf-8">
<title>Covid-19 Phased Exit Strategy</title>
<link rel="stylesheet" href="https://fonts.googleapis.com/css2?family=Montserrat:wght@900&family=Fira+Sans:wght@400;700;800&family=Source+Sans+3:wght@300;400&display=swap">
<style>
  :root {
    --red: #e52629;
    --blue: #49a8de;
    --yellow: #f8c11a;
    --ink: #1d1d1b;
    --white: #ffffff;
    --rule: #8a8a8a;
    --grey-left: #d9d9d9;
    --grey-right: #ffffff;
  }
  * { margin: 0; padding: 0; box-sizing: border-box; }
  html, body { width: 1200px; height: 2400px; overflow: hidden; }
  body {
    position: relative;
    background: var(--white);
    font-family: "Source Sans 3", Arial, sans-serif;
    color: var(--ink);
  }
  .header {
    position: absolute; left: 0; top: 0; width: 1200px; height: 371px;
    background: var(--red); color: var(--white); text-align: center;
  }
  .header__title {
    position: absolute; left: 0; right: 0; top: 40px;
    font-family: "Montserrat", sans-serif; font-weight: 900;
    font-size: 70px; line-height: 74px; letter-spacing: 1px;
  }
  .header__subtitle {
    position: absolute; left: 0; right: 0; top: 116px;
    font-family: "Fira Sans", sans-serif; font-weight: 700;
    font-size: 38px; line-height: 42px; letter-spacing: 0.5px;
  }
  .header__author {
    position: absolute; left: 0; right: 0; top: 161px;
    font-family: "Fira Sans", sans-serif; font-weight: 400;
    font-size: 31px; line-height: 36px;
  }
  .header__intro {
    position: absolute; left: 48px; right: 48px; top: 214px;
    font-size: 20.5px; line-height: 25px;
  }
  .requirements {
    position: absolute; left: 0; top: 371px; width: 1200px; height: 285px;
    background: var(--blue); color: var(--ink); text-align: center;
  }
  .requirements__title {
    position: absolute; left: 0; right: 0; top: 10px;
    font-weight: 300; font-size: 46px; line-height: 52px; color: #1a2a3a;
  }
  .requirements__list {
    position: absolute; left: 55px; right: 55px; top: 70px;
    list-style: none; font-size: 14.4px; line-height: 18.3px;
  }
  .plan {
    position: absolute; left: 0; top: 656px; width: 1200px; height: 1700px;
    background: linear-gradient(90deg, var(--grey-left), var(--grey-right) 60%);
  }
  .plan__title {
    position: absolute; left: 0; right: 0; top: 8px; text-align: center;
    font-family: "Fira Sans", sans-serif; font-weight: 800;
    font-size: 39px; line-height: 44px; color: var(--red);
    display: flex; justify-content: center; align-items: center; gap: 14px;
  }
  .gear { width: 28px; height: 28px; }
  .stage-rule {
    position: absolute; left: 0; width: 1200px; height: 1px; background: var(--rule);
  }
  .stage-label {
    position: absolute; left: 481px; width: 239px; height: 41px;
    background: var(--yellow); text-align: center;
    font-weight: 300; font-size: 42px; line-height: 41px; color: var(--ink);
  }
  .stage-entry {
    position: absolute; left: 52px; right: 52px; text-align: center;
    font-family: "Fira Sans", sans-serif; font-weight: 700;
    font-size: 19.4px; line-height: 25px;
  }
  .stage-steps {
    position: absolute; left: 48px; right: 48px; text-align: center;
    list-style: none; font-size: 14.4px; line-height: 18.3px;
  }
  .band-red { position: absolute; left: 0; top: 2356px; width: 1200px; height: 23px; background: var(--red); }
  .band-blue { position: absolute; left: 0; top: 2379px; width: 1200px; height: 21px; background: var(--blue); }
</style>
</head>
<body>

<header class="header">
  <h1 class="header__title">COVID-19</h1>
  <h2 class="header__subtitle">PHASED EXIT STRATEGY</h2>
  <p class="header__author">DEVELOPED BY LENA FARROW</p>
  <p class="header__intro">Pandemics have, historically, seen their end both medically - via herd immunity or immunizations. And while there are several clinical trials underway for potential Covid-19 vaccines, we are still a long way from deploying an effective vaccine and one that will stand the test of time as the virus changes. Covid-19 pandemic will be considered 'ended’ when there are only occasional traces of localized cases that are quickly contained in specific locations., Today and in the absence of an effective vaccine(s) and for the re-opening of the economies and social activities to be successful, it is critical that the following basic conditions be in place before any lockdowns are lifted and before social activities resume:</p>
</header>

<section class="requirements">
  <h2 class="requirements__title">GENERAL REQUIREMENTS</h2>
  <ol class="requirements__list">
    <li>1. Single digit downward trend of documented cases within the past 14-days.</li>
    <li>2. Hospitals and the health care system are capable of treating patients without operating on a crisis mode.</li>
    <li>3. Ability to screen and test symptomatic individuals within 24 hours of identification. Increased and sufficient testing capacity, to test at least 50% of all population if necessary within a timeframe of 3 months.</li>
    <li>4. Ability to surge ICU capacity on a short notice - 24h.</li>
    <li>5. Ability to track and trace infected patients and contacts on a live basis and across the country and ability to react quickly to any unusual trends or outbreaks.</li>
    <li>6. Plan in place to trigger targeted or full-scale containment in case of sudden outbreaks</li>
    <li>7. Mandatory use of masks (at least surgical grade) for everyone in all public areas and at work. Mandatory use of N95, or equivalent, masks for all healthcare front workers and for all government agencies and authorities that are involved in overseeing the containment activities.</li>
    <li>8. Mandatory daily checks of body temperature for everyone at the workplace or entering public areas.</li>
    <li>9. Mandatory sanitation in all places - use of disinfection available on a large scale.</li>
  </ol>
</section>

<main class="plan">
  <h2 class="plan__title">
    <svg class="gear" viewBox="0 0 28 28" aria-hidden="true"><circle cx="14" cy="14" r="10.5" fill="none" stroke="#49a8de" stroke-width="5" stroke-dasharray="4.1 4.1"/><circle cx="14" cy="14" r="8" fill="#49a8de"/><circle cx="14" cy="14" r="3.5" fill="#eeeeee"/></svg>
    Phased Covid-19 Lockdown Exit Strategy Plan
    <svg class="gear" viewBox="0 0 28 28" aria-hidden="true"><circle cx="14" cy="14" r="10.5" fill="none" stroke="#49a8de" stroke-width="5" stroke-dasharray="4.1 4.1"/><circle cx="14" cy="14" r="8" fill="#49a8de"/><circle cx="14" cy="14" r="3.5" fill="#ffffff"/></svg>
  </h2>

  <div class="stage-rule" style="top:80px"></div>
  <div class="stage-label" style="top:60px">STAGE 1</div>
  <p class="stage-entry" style="top:101px">To enter this stage, additional to the general requirements, the Effective Reproduction Number (Rt) must be less than 1 and the death rate at less than 3%. The economy and social activities can resume in this sequence:</p>
  <ol class="stage-steps" style="top:168px">
    <li>a. Elderly (60+ years old) and vulnerable individuals should continue to self-isolate.</li>
    <li>b. No more than 5 people maximum gathering at a time in public areas and at work.</li>
    <li>c. Work from home should continue whenever and as much as possible.</li>
    <li>d. Social distancing should continue to be re-enforced in public areas, at work and in all areas reopened.</li>
    <li>e. Non-essential travel should be minimized between cities and regions (and within cities and regions where covid-19 infections are still a risk)</li>
    <li>f. Large businesses (300 people and more, manufacturing, services, etc.) can reopen progressively. Common areas should remain closed (cafeteria, restaurant, gym, meeting rooms of no more than 5 people).</li>
    <li>g. Small businesses (300 people and less) can reopen as well with the same conditions as large businesses.</li>
    <li>h. Commercial shops can reopen. Shops should control the flow of people in their facilities not to exceed 30% at a time of standard capacity. Shops should provide disinfectant and temperature control at entry.</li>
    <li>i. Pharmacies will continue to be open. However, they must make available disinfectant for use by clients and will continue to comply with social distancing. Pharmacies should limit the number of client/patient in<br>their stores not to exceed 30% of the standard capacity.</li>
    <li>j. Transportation (buses, taxis, airlines) will resume progressively. No air travels permitted in and out of Covid-19 known hotspots, locally or internationally. Entry to country should be limited and strictly controlled. All landing passengers and visitors regardless of the country of origin should be tested for Covid-19 at arrival. All passengers and visitors will undergo a temperature check at arrival. No more than 3 people at a time in a taxi/zipride including the driver. All passengers wearing masks. Buses should operate with no more than 30% customer’s capacity per bus.</li>
    <li>k. Religious sites can reopen with a maximum capacity of 30% or less. Social distancing and wearing masks is mandatory. Religious sites should organize (volunteers can help) to check body temperature of everyone accessing the site and provide disinfectant at entry.</li>
    <li>l. Hotels &amp; tourism (museums, etc.) can reopen but must operate at 30% or less capacity. All common areas (restaurants, gyms, swimming pools, conference rooms, etc.) should remain closed.</li>
    <li>m. Coffee &amp; restaurants can reopen but must operate at 30% capacity as well and comply with social distancing. Clients must wear as much as possible their masks if they are not consuming food/coffee. Clients should avoid to talking to each other with masks off.</li>
    <li>n. All schools should remain closed. On-line courses should continue be the preferred method for education.</li>
    <li>o. Large scale events (cinema, theaters, sport, business conferences, etc.) should remain closed or operate virtually. Sport events can resume but without spectators. Athletes and the staff surrounding them should be tested, disinfectants should be available and masks used as much as reasonably possible.</li>
  </ol>

  <div class="stage-rule" style="top:680px"></div>
  <div class="stage-label" style="top:660px">STAGE 2</div>
  <p class="stage-entry" style="top:700px">To enter stage 2 of the Covid-19 Exit Strategy, compliance to the general requirements is compulsory, additional to a successful Stage 1 outcome. The Effective Reproduction Number (Rt) for Stage 2 must be less than 0.5 and the death rate stabilized at less than 1.5%. The economy and social activities can resume in this sequence:</p>
  <ol class="stage-steps" style="top:792px">
    <li>a. Elderly (60+ years old) and vulnerable individuals should continue to self-isolate as much as possible. If</li>
    <li>b. No more than 10 people maximum gathering at a time in public areas and at work.</li>
    <li>c. Work from home should if possible or for jobs that do not have to be necessarily in an office setup.</li>
    <li>d. Social distancing can be relaxed. However people should continue to wear masks and use disinfectants.</li>
    <li>e. Travel can resume between cities and regions. The same containment restrictions should apply to any existing hotspot.</li>
    <li>f. Elective surgeries can resume in hospitals and clinics that are equipped to comply with all general requirements.</li>
    <li>g. Large businesses (300 people and more, manufacturing, services, etc.) will continue to operate. Common areas should open but social<br>distancing should remain (cafeteria, restaurant, gym, meeting rooms of no more than 10 people).</li>
    <li>h. Small businesses (300 people and less) will continue to operate with the same conditions as large businesses.</li>
    <li>i. Commercial shops will continue to be open and can operate at 50% capacity. Wear of masks should continue.</li>
    <li>j. Pharmacies will continue to be open and will need to operate a 50% capacity</li>
    <li>k. Transportation (buses, taxis, and airlines) will continue to operate. Still no air travels permitted in and out of Covid-19 known hotspots, locally or internationally. Entry to country should be relaxed but remain controlled. Airports should continue to use thermo cameras to monitor passenger’s temperature at landing. Airports should be equipped to test for Covid-19 if necessary. Transportation by taxi/zipride continues, however, passengers wear masks. Buses could operate with 50% capacity per bus.</li>
    <li>l. Religious sites can operate with a maximum capacity of 50%. Social distancing and wearing masks should be enforced. Sites should continue to check body temperature of everyone accessing the site and provide disinfectant at entry.</li>
    <li>m. Hotels &amp; tourism (museums, etc.) can operate at 50% capacity. All common areas (restaurants, gyms, swimming pools, conference rooms, etc.) could reopen. Gatherings are limited to 10 people or less and can be expanded with social distancing and wearing protective masks.</li>
    <li>n. Coffee &amp; restaurants can operate at 50% capacity and continue comply with social distancing. Clients must wear as much as possible their<br>masks if they are not consuming food/coffee.</li>
    <li>o. Schools can reopen in parallel with on-line education. Social distancing and re-arranging school seating to prevent the spread of infection is mandatory.</li>
    <li>p. Large scale events (cinema, theaters, sport, business conferences, etc.) could resume under strict social distancing. People should wear masks.</li>
  </ol>

  <div class="stage-rule" style="top:1230px"></div>
  <div class="stage-label" style="top:1210px">STAGE 3</div>
  <p class="stage-entry" style="top:1250px">To enter stage 3 of the Covid-19 Exit Strategy, compliance to the general requirements is compulsory, additional to a successful Stage 2 outcome. The Effective Reproduction Number (Rt) for Stage 3 must be less than 0.3 and the death rate stabilized at less than 1%. The economy and social activities can resume in this sequence:</p>
  <ol class="stage-steps" style="top:1342px">
    <li>a. Elderly (60+ years old) and vulnerable individuals may resume all previously exercised activities without restrictions.</li>
    <li>b. Restrictions as to the number of people gathering together can be lifted. Social distancing can be relaxed. However, wear of masks may continue.</li>
    <li>c. Travel can resume between cities and regions and out of country travel. The same containment restrictions as Stage 1 and 2 would continue to apply to any existing hotspot.</li>
    <li>d. All hospital and clinic surgeries can resume in hospitals in compliance with standard hospital and health care procedures.</li>
    <li>e. Large businesses (300 people and more, manufacturing, services, etc.) will resume normal business practices. Wear of masks is recommended but not mandatory.</li>
    <li>f. Small businesses (300 people and less) will operate with the same conditions as large businesses.</li>
    <li>g. Commercial shops can operate on a normal mode - previous to covid-19. Wear of masks could be recommended in certain areas.</li>
    <li>h. Pharmacies can operate at a normal state.</li>
    <li>i. Transportation (buses, taxis, and airlines) will operate at a normal capacity. Still no air travels permitted in and out of Covid-19 known hotspots, locally or internationally. Entry to country should be relaxed and operate normally. Airports should continue to use thermo cameras to monitor passenger’s temperature at landing. Airports should be equipped to test for Covid-19 if necessary. Transportation by taxi/zipride and buses will resume on a normal mode. Wear of masks is elective.</li>
    <li>j. Religious sites can operate normally. Wear of masks should be elective.</li>
    <li>k. Hotels &amp; tourism (museums, etc.) can operate at 100% capacity including all common areas</li>
    <li>l. Coffee &amp; restaurants can resume normal operations. Clients may wear masks for personal protection if they wish to.</li>
    <li>m. Schools can resume operations. Re-arranging school seating should continue until a vaccine is found.</li>
    <li>n. Large scale events (cinema, theaters, sport, business conferences, etc.) could resume under moderate social distancing. People may elect to wear masks.</li>
  </ol>
</main>

<div class="band-red"></div>
<div class="band-blue"></div>

</body>
</html>
```